Young Accounting firm needing a captivating business card

We need a business card design that forces the person to look at the card because its either gold foil, plastic, or lettering pop up etc. We already have a logo with a specific gold color and we need to make it pop. We are an accounting firm. I need the words" accounting, payroll, licenses, audits, taxes" somewhere on the business card so as to describe what we do- preferably on the side where the logo is at.

Industry/Entity Type

Accounting

Contact Information for Business Card

Address 48276 9th Ave S Ste 305, Federal Way, WA 98117
Business Phone (360)418-2096
Fax (360)418-2157
Office Cell Phone (360)586-7319

Font styles to use
Serif

Colors
85abd2

Requirements
Must have
• It should state
• "Accounting" "Taxes" "Audits" "Licenses" "Payroll"
Nice to have
• Matte with gold foil, different textures, With Either a textured ivory background or gray blue slate background
Should not have
• colorful colors

```html
<!DOCTYPE html>
<html lang="en">
<head>
<meta charset="utf-8">
<title>Ledgerwise Business Card</title>
<link rel="stylesheet" href="https://fonts.googleapis.com/css2?family=Montserrat:wght@400;500;700&family=Oswald:wght@400&display=swap">
<style>
  :root {
    --backdrop: #2a2c30;
    --card: #1e1f22;
    --card-back: #141416;
    --gold: #c9a227;
    --gold-bright: #d9b431;
    --blue: #85abd2;
    --slate: #8ea4bd;
    --white: #f2f2f2;
  }
  * { box-sizing: border-box; margin: 0; padding: 0; }
  html, body { width: 1200px; height: 900px; overflow: hidden; }
  body {
    background: var(--backdrop);
    font-family: "Montserrat", sans-serif;
    display: flex;
    flex-direction: column;
    align-items: center;
    justify-content: center;
    gap: 40px;
  }
  .card {
    position: relative;
    width: 700px;
    height: 400px;
    border-radius: 4px;
    overflow: hidden;
    box-shadow: 0 12px 30px rgba(0,0,0,0.45);
  }
  .card-front { background: var(--card); }

  .brand-block {
    position: absolute;
    left: 40px;
    top: 70px;
    width: 290px;
    display: flex;
    flex-direction: column;
    align-items: center;
    gap: 18px;
  }
  .brand-mark {
    width: 64px;
    height: 64px;
    background: var(--gold);
  }
  .brand-name {
    font-weight: 500;
    font-size: 44px;
    letter-spacing: -1px;
    color: var(--gold);
  }
  .divider {
    position: absolute;
    left: 355px;
    top: 70px;
    width: 2px;
    height: 170px;
    background: var(--gold);
  }
  .contact-block {
    position: absolute;
    left: 378px;
    top: 72px;
  }
  .person-name {
    font-weight: 700;
    font-size: 30px;
    color: var(--blue);
    line-height: 1.05;
  }
  .person-title {
    font-size: 19px;
    color: var(--gold);
    margin-bottom: 6px;
  }
  .contact-row {
    display: flex;
    align-items: center;
    gap: 8px;
    font-size: 19px;
    color: var(--gold);
    line-height: 1.3;
  }
  .contact-row svg { width: 16px; height: 16px; flex: none; }
  .icon { fill: var(--blue); }

  .address-line {
    position: absolute;
    left: 0;
    right: 0;
    top: 296px;
    display: flex;
    align-items: center;
    gap: 20px;
  }
  .accent-bar { height: 18px; background: var(--gold); }
  .accent-bar.left { width: 70px; }
  .accent-bar.right { width: 95px; margin-left: auto; }
  .address {
    font-size: 20px;
    color: var(--slate);
    white-space: nowrap;
  }

  .card-back { background: var(--card-back); }
  .pattern-field {
    position: absolute;
    inset: 0;
    background: linear-gradient(135deg, #232326 0%, #1a1a1c 55%, #141416 100%);
  }
  .back-brand {
    position: absolute;
    right: 150px;
    top: 150px;
    display: flex;
    align-items: center;
    gap: 12px;
  }
  .back-brand .brand-mark { width: 44px; height: 44px; background: var(--gold-bright); }
  .back-brand .brand-name { font-size: 34px; color: var(--gold-bright); }
  .services {
    position: absolute;
    left: 40px;
    top: 250px;
    font-family: "Oswald", sans-serif;
    font-style: italic;
    font-size: 20px;
    letter-spacing: 1.5px;
    color: var(--white);
  }
</style>
</head>
<body>
  <section class="card card-front">
    <div class="brand-block">
      <div class="brand-mark"></div>
      <div class="brand-name">Ledgerwise</div>
    </div>
    <div class="divider"></div>
    <div class="contact-block">
      <div class="person-name">Marcus Hale</div>
      <div class="person-title">Founder &amp; CEO</div>
      <div class="contact-row">
        <svg viewBox="0 0 16 16"><path class="icon" d="M2 6c0-2 3-4 6-4s6 2 6 4v1h-3V6H5v1H2zM4 8h8l1 6H3z"/></svg>
        <span>(360) 418-2096</span>
      </div>
      <div class="contact-row">
        <svg viewBox="0 0 16 16"><rect class="icon" x="4" y="1" width="8" height="14" rx="1.5"/><rect x="5.5" y="3" width="5" height="8" fill="#1e1f22"/></svg>
        <span>(360) 586-7319</span>
      </div>
      <div class="contact-row">
        <svg viewBox="0 0 16 16"><rect class="icon" x="4" y="1" width="8" height="5"/><rect class="icon" x="1" y="7" width="14" height="6" rx="1"/><rect class="icon" x="4" y="13" width="8" height="2"/></svg>
        <span>(360) 418-2157</span>
      </div>
      <div class="contact-row">
        <svg viewBox="0 0 16 16"><rect class="icon" x="1" y="3" width="14" height="10"/><path d="M1 3l7 6 7-6" fill="none" stroke="#1e1f22" stroke-width="1.5"/></svg>
        <span>info@ledgerwisetax.com</span>
      </div>
    </div>
    <div class="address-line">
      <div class="accent-bar left"></div>
      <span class="address">48276 9th Ave S Ste 305, Federal Way, WA 98117</span>
      <div class="accent-bar right"></div>
    </div>
  </section>

  <section class="card card-back">
    <div class="pattern-field" role="img" aria-label="Faint tone-on-tone repeating emblem pattern across the dark card"></div>
    <div class="back-brand">
      <div class="brand-mark"></div>
      <div class="brand-name">Ledgerwise</div>
    </div>
    <div class="services">ACCOUNTING, PAYROLL, LICENSES, AUDITS, TAXES</div>
  </section>
</body>
</html>
```